Cryptocurrency Advisor Business Card

Dravelin Consulting Services is my company, which advises many projects in the ICO/Cryptocurrency industry. I'd like to get a sleek, preferably matte black or matte dark blue finish, business card with the company name (and simple logo w/ crypto feel) on one side and while the other side I'd like a small twitter and telegram logo together maybe separated by a / as it's the same, then an email and a phone logo so I can insert those specifics there (no address). Can have name then CEO section too. At the bottom of that section, find a place for more of a job description: ICO Advisor, World Champion Gamer, Esports Award Winner, Quorvane Expert. You can possibly design a simple logo or use something with a crypto twist or background, but nothing too complex. Rounded edges for printing not square.
Updates

Had personal issues taking a few days away from me being able to provide feedback and check designs, etc. Will be more active now finalizing design just needed few days from issue but all is sorted.

Target Market(s)

Cryptocurrency industry

Industry/Entity Type

Management Consulting

Contact Information for Business Card

Font styles to use
Sans Serif

Colors
5c5c5c
474747
757575
9d9d9d
aaaaaa
333333
0355a3

Requirements
Must have
• Refer to Details/Description
Nice to have
Should not have
• Address section

```html
<!DOCTYPE html>
<html lang="en">
<head>
<meta charset="utf-8">
<title>Dravelin Consulting Services – Business Card</title>
<link rel="stylesheet" href="https://fonts.googleapis.com/css2?family=Roboto:wght@300;400;700&display=swap">
<style>
  :root {
    --page-bg: #e6e7e9;
    --card-white: #ffffff;
    --brand-blue: #0355a3;
    --ink: #333333;
    --muted: #5c5c5c;
    --map-faint: #eef0f7;
    --navy-deep: #0b2738;
    --navy-light: #2f3c66;
    --map-navy: #2a5578;
    --white: #ffffff;
  }
  * { box-sizing: border-box; margin: 0; padding: 0; }
  html, body {
    width: 1200px; height: 868px; overflow: hidden;
    background: var(--page-bg);
    font-family: "Roboto", Arial, sans-serif;
  }
  .canvas { position: relative; width: 1200px; height: 868px; }

  .card {
    position: absolute; top: 286px;
    width: 504px; height: 296px;
    border-radius: 32px; overflow: hidden;
  }
  .card--front { left: 78px; background: var(--card-white); }
  .card--back {
    left: 619px;
    background: linear-gradient(200deg, var(--navy-light) 0%, #1f3352 55%, var(--navy-deep) 100%);
  }

  .world-map {
    position: absolute; left: 16px; top: 16px; width: 480px; height: 250px;
    border-radius: 40% 45% 38% 42%;
  }
  .card--front .world-map {
    background: radial-gradient(ellipse at center, var(--map-faint) 0%, rgba(238,240,247,0.6) 60%, rgba(238,240,247,0) 100%);
  }
  .card--back .world-map {
    background: radial-gradient(ellipse at center, rgba(42,85,120,0.75) 0%, rgba(42,85,120,0.45) 60%, rgba(42,85,120,0) 100%);
  }

  .person { position: absolute; left: 44px; top: 38px; display: inline-block; }
  .person__name {
    font-size: 30px; font-weight: 700; color: var(--brand-blue);
    letter-spacing: -0.3px; line-height: 1;
  }
  .person__title {
    display: block; text-align: right;
    font-size: 21px; font-weight: 300; color: var(--muted);
    line-height: 1; margin-top: 4px; letter-spacing: 0.5px;
  }

  .job-description {
    position: absolute; left: 44px; top: 114px;
    font-size: 12px; font-weight: 300; color: var(--brand-blue); line-height: 15px;
  }

  .contact-list { position: absolute; left: 44px; top: 198px; list-style: none; }
  .contact-list li {
    display: flex; align-items: center; height: 19.6px;
    font-size: 14.5px; color: var(--ink); font-weight: 400;
  }
  .contact-list .icon { width: 14px; height: 14px; margin-left: 2px; margin-right: 16px; flex: none; }
  .icon-dot { fill: var(--brand-blue); }

  .brand {
    position: absolute; left: 0; right: 0; top: 104px; text-align: center;
  }
  .brand__mark {
    display: block; margin: 0 auto 22px;
    width: 40px; height: 40px; border-radius: 50%;
    background: var(--white);
  }
  .brand__name { font-size: 24px; font-weight: 400; color: var(--white); letter-spacing: 0.1px; }
</style>
</head>
<body>
<main class="canvas">

  <section class="card card--front" aria-label="Card front">
    <div class="world-map" role="img" aria-label="Faint world map background"></div>
    <div class="person">
      <h1 class="person__name">Aldren Voss</h1>
      <span class="person__title">C.E.O</span>
    </div>
    <p class="job-description">ICO Advisor, World Champion Gamer,<br>Esports Award Winner, QuorvaneExpert.</p>
    <ul class="contact-list">
      <li>
        <svg class="icon" viewBox="0 0 14 14" aria-hidden="true">
          <rect x="0.5" y="3" width="13" height="8.5" fill="var(--brand-blue)"/>
          <path d="M0.5 3 L7 8 L13.5 3" stroke="#fff" stroke-width="1.2" fill="none"/>
        </svg>youremail@email.com
      </li>
      <li>
        <svg class="icon" viewBox="0 0 14 14" aria-hidden="true">
          <path d="M3 1.5 L5.2 1.5 L6 4.5 L4.6 5.6 C5.4 7.4 6.6 8.6 8.4 9.4 L9.5 8 L12.5 8.8 L12.5 11 C12.5 12 11.7 12.6 10.8 12.5 C6 12 2 8 1.5 3.2 C1.4 2.3 2 1.5 3 1.5 Z" fill="var(--brand-blue)"/>
        </svg>111-222-333-555
      </li>
      <li>
        <svg class="icon" viewBox="0 0 14 14" aria-hidden="true"><circle class="icon-dot" cx="7" cy="7" r="5.5"/></svg>yourfeedaccount
      </li>
      <li>
        <svg class="icon" viewBox="0 0 14 14" aria-hidden="true"><circle class="icon-dot" cx="7" cy="7" r="5.5"/></svg>yourmessenger
      </li>
    </ul>
  </section>

  <section class="card card--back" aria-label="Card back">
    <div class="world-map" role="img" aria-label="World map background in muted blue"></div>
    <div class="brand">
      <span class="brand__mark" aria-hidden="true"></span>
      <h2 class="brand__name">Dravelin Consulting Services</h2>
    </div>
  </section>

</main>
</body>
</html>
```